Marlow 2400 - KR Layouts
Harold Pinkney
Project: Marlow 2400 - KR Layouts
Creative Brief
Printing
Banks and Credit Unions, Corporate, would appeal to their customers.
1) Each designer should submit 3 different designs under the category "Customer Appreciation." Visit this page to see past designs: http://www.marlow2400.example/exclusive-images/customer-appreciation/. The designs can share comment graphical elements (such as color scheme or layout), but must be different. 2) Please use pixavane.example as your image source (just download the comp image and we will purchase the final image once design is complete). 3) Size = 3.125"w x 7"h 4) No bleeds 5) You can use your own copy or reuse some that are on the http://www.marlow2400.example/exclusive-images/customer-appreciation/.

```html
<!DOCTYPE html>
<html lang="en">
<head>
<meta charset="utf-8">
<title>Customer Appreciation</title>
<link rel="stylesheet" href="https://fonts.googleapis.com/css2?family=Cormorant+Garamond:wght@500&display=swap">
<style>
  :root {
    --backdrop: #4a3b2c;
    --card: #ffffff;
    --crimson: #a41c24;
    --crimson-deep: #8f151c;
    --crimson-bright: #d9252f;
    --ember: #e0622e;
    --ember-soft: #c9402a;
    --ink: #3a3a3a;
  }
  html, body {
    margin: 0;
    width: 1200px;
    height: 904px;
    overflow: hidden;
    background: var(--backdrop);
  }
  .card {
    position: absolute;
    left: 421px;
    top: 42px;
    width: 365px;
    height: 820px;
    background: var(--card);
    overflow: hidden;
  }
  .crown-art {
    position: absolute;
    left: 64px;
    top: 56px;
    width: 237px;
    height: 238px;
    background:
      radial-gradient(ellipse 42% 26% at 50% 50%, var(--ember) 0%, var(--ember-soft) 55%, rgba(164, 28, 36, 0) 100%),
      radial-gradient(circle at 50% 50%, var(--crimson) 55%, var(--crimson-deep) 100%);
  }
  .card-title {
    position: absolute;
    left: 0;
    right: 0;
    top: 312px;
    margin: 0;
    text-align: center;
    font-family: "Cormorant Garamond", Georgia, serif;
    font-weight: 500;
    font-size: 25px;
    line-height: 1.2;
    color: var(--ink);
    letter-spacing: 0.2px;
  }
  .bottom-wave {
    position: absolute;
    left: 0;
    bottom: 0;
    width: 365px;
    height: 176px;
    display: block;
  }
</style>
</head>
<body>
  <div class="card">
    <div class="crown-art" role="img" aria-label="Glowing crown built from small gift and star icons on a deep red square"></div>
    <h1 class="card-title">Customer Appreciation</h1>
    <svg class="bottom-wave" viewBox="0 0 365 176" aria-hidden="true">
      <path d="M0 146 Q 215 150 365 12" fill="none" stroke="var(--crimson-bright)" stroke-width="4"/>
      <path d="M0 158 Q 225 164 365 36 L365 176 L0 176 Z" fill="var(--crimson)"/>
    </svg>
  </div>
</body>
</html>
```